<作成物>
■リッチメッセージ
リッチメニュー
合計2枚
リッチメニュー の表示項目は画像写真添付します。
写真添付しております。

【デザインの詳細】
オレンジ(画像の女性のエプロンのオレンジと似せてください)
をベースに元気でハッピーになれるような感じを希望しております。
使用される画像は添付のアドレスに入ってりますの
でどれを使用されても構いません。
イメージのデザイン合わせた感じにしていただけると嬉しいです。
https://files.tovrelink-share.example/dl/5k2m9q7x3c8v1b4n6z0p
上下で一体感があるものを希望します。
人物の画像は入れても入れなくても(デザインで決めてください)

【表示文言】
上の画像に入れる文言
工作感覚で作るから初めてでも大丈夫!
可愛い過ぎるお寿司レッスン
(文字がデザイン的に合わなければ入れなくてもOK)

〈リッチメニューの表示項目〉
画像の中に入れますの、これを参考に入れてください。

デザイン重視でここの表示名はデザイン的に英語の方がよければ
英語でも大丈夫です。意味がわかって
ニュアンスがあっていれば文字を短くするのも
お任せします。あくまでデザイン重視です。
〈画像はこちらから〉
画像

※こちらの作成以外に勝手に使用された場合は
著作権侵害で法的手段をとらせていただきます。
作成事例にもしようしないでください。

<サイズ>
・リッチメッセージ(1040×1040ピクセル)
・リッチメニュー(1200×810ピクセル)

<納品形式>
・ai形式(イラストレーターデータ)
・JPG
<詳細>
※添付ファイルをご確認ください。

<備考>
ブランディング効果を期待しています。
どんどん何個でも応募ください。

```html
<!DOCTYPE html>
<html lang="ja">
<head>
<meta charset="utf-8">
<title>可愛い過ぎるお寿司レッスン｜リッチメニュー</title>
<link rel="stylesheet" href="https://fonts.googleapis.com/css2?family=M+PLUS+Rounded+1c:wght@500;800&family=Kosugi+Maru&display=swap">
<style>
  :root{
    --stage:#e4e3e1;
    --white:#ffffff;
    --orange:#f08a24;
    --orange-deep:#e5711a;
    --orange-soft:#f4a24a;
    --yellow:#f6c24c;
    --yellow-soft:#f8d27a;
    --cream:#fff6e8;
    --photo-a:#f3e7dc;
    --photo-b:#e9c9a8;
    --photo-c:#d9a77a;
    --text-orange:#f07d12;
  }
  *{box-sizing:border-box;margin:0;padding:0}
  html,body{width:803px;height:1200px;overflow:hidden;background:var(--stage)}
  body{position:relative;font-family:"M PLUS Rounded 1c","Kosugi Maru",sans-serif}
  .rich-menu{
    position:absolute;left:94px;top:75px;width:629px;height:1052px;
    background:var(--white);box-shadow:0 2px 10px rgba(0,0,0,.12);overflow:hidden;
  }
  .hero{position:absolute;left:0;top:0;width:629px;height:617px}
  .hero-photo{
    position:absolute;inset:0;
    background:
      radial-gradient(ellipse 200px 260px at 440px 300px, var(--photo-b), transparent 70%),
      radial-gradient(ellipse 160px 110px at 130px 540px, #e8a6a6, transparent 72%),
      radial-gradient(ellipse 180px 90px at 520px 580px, var(--photo-c), transparent 70%),
      linear-gradient(180deg, var(--photo-a) 0%, #efe0d0 60%, #e6cdb4 100%);
  }
  .catch{
    position:absolute;left:40px;top:92px;transform:rotate(-16deg);transform-origin:left top;
    color:var(--text-orange);font-weight:800;font-size:27px;line-height:1.35;
    text-shadow:0 0 4px var(--white),0 0 4px var(--white),0 0 4px var(--white);
  }
  .catch span{display:block}
  .catch span:last-child{padding-left:60px}
  .title{
    position:absolute;left:66px;top:265px;color:var(--text-orange);font-weight:800;
    line-height:1.08;letter-spacing:2px;
    text-shadow:0 0 5px var(--white),0 0 5px var(--white),0 0 6px var(--white),0 0 6px var(--white);
  }
  .title .small{display:block;font-size:44px}
  .title .large{display:block;font-size:74px;padding-left:20px}
  .title .mid{display:block;font-size:62px;padding-left:20px}
  .menu-grid{
    position:absolute;left:0;top:617px;width:629px;height:435px;
    display:grid;grid-template-columns:repeat(3,1fr);grid-template-rows:repeat(2,1fr);
    gap:5px;background:var(--white);padding:5px 0 0;
  }
  .tile{
    display:flex;flex-direction:column;align-items:center;justify-content:center;gap:10px;
    color:var(--white);text-decoration:none;
  }
  .tile--orange{background:linear-gradient(160deg,var(--orange-soft),var(--orange))}
  .tile--yellow{background:linear-gradient(160deg,var(--yellow-soft),var(--yellow))}
  .tile--amber{background:linear-gradient(160deg,#f6b45a,var(--orange-soft))}
  .tile-icon{width:86px;height:86px}
  .tile-label{font-size:24px;font-weight:800;line-height:1;text-align:center}
  .tile-label small{display:block;font-size:13px;font-weight:500;margin-top:4px}
</style>
</head>
<body>
  <main class="rich-menu">
    <section class="hero">
      <div class="hero-photo" role="img" aria-label="オレンジのエプロン姿の講師が飾り巻き寿司を持つ写真と、手前に並ぶ花柄の飾り巻き寿司"></div>
      <p class="catch"><span>工作感覚で作るから</span><span>初めてでも大丈夫!</span></p>
      <h1 class="title">
        <span class="small">可愛い過ぎる</span>
        <span class="large">お寿司</span>
        <span class="mid">レッスン</span>
      </h1>
    </section>

    <nav class="menu-grid">
      <a class="tile tile--orange" href="#menu">
        <svg class="tile-icon" viewBox="0 0 86 86" fill="none" stroke="#fff" stroke-width="3">
          <rect x="2" y="2" width="82" height="82" rx="16"/>
          <rect x="26" y="20" width="34" height="46" rx="4"/>
          <line x1="33" y1="32" x2="53" y2="32"/><line x1="33" y1="42" x2="53" y2="42"/><line x1="33" y1="52" x2="46" y2="52"/>
        </svg>
        <span class="tile-label">Menu</span>
      </a>
      <a class="tile tile--yellow" href="#schedule">
        <svg class="tile-icon" viewBox="0 0 86 86" fill="none" stroke="#fff" stroke-width="3">
          <rect x="2" y="2" width="82" height="82" rx="16"/>
          <rect x="20" y="24" width="46" height="40" rx="4"/>
          <line x1="20" y1="34" x2="66" y2="34"/><line x1="31" y1="18" x2="31" y2="28"/><line x1="55" y1="18" x2="55" y2="28"/>
          <g fill="#fff" stroke="none"><circle cx="31" cy="44" r="2.5"/><circle cx="43" cy="44" r="2.5"/><circle cx="55" cy="44" r="2.5"/><circle cx="31" cy="54" r="2.5"/><circle cx="43" cy="54" r="2.5"/></g>
        </svg>
        <span class="tile-label">Schedule</span>
      </a>
      <a class="tile tile--orange" href="#event">
        <svg class="tile-icon" viewBox="0 0 86 86" fill="none" stroke="#fff" stroke-width="3">
          <rect x="2" y="2" width="82" height="82" rx="16"/>
          <rect x="20" y="24" width="46" height="40" rx="4"/>
          <line x1="20" y1="34" x2="66" y2="34"/><line x1="31" y1="18" x2="31" y2="28"/><line x1="55" y1="18" x2="55" y2="28"/>
          <path d="M43 39l3.5 7 7.5 1-5.5 5 1.5 7.5L43 56l-7 3.5 1.5-7.5-5.5-5 7.5-1z" fill="#fff" stroke="none"/>
        </svg>
        <span class="tile-label">Event</span>
      </a>
      <a class="tile tile--yellow" href="#homepage">
        <svg class="tile-icon" viewBox="0 0 86 86" fill="none" stroke="#fff" stroke-width="3">
          <rect x="2" y="2" width="82" height="82" rx="16"/>
          <circle cx="43" cy="43" r="22"/><circle cx="43" cy="43" r="6" fill="#fff"/>
          <circle cx="43" cy="30" r="5"/><circle cx="43" cy="56" r="5"/><circle cx="30" cy="43" r="5"/><circle cx="56" cy="43" r="5"/>
        </svg>
        <span class="tile-label">Home Page</span>
      </a>
      <a class="tile tile--orange" href="#sns">
        <svg class="tile-icon" viewBox="0 0 86 86" fill="none" stroke="#fff" stroke-width="3">
          <rect x="2" y="2" width="82" height="82" rx="16"/>
          <path d="M22 26h42a4 4 0 0 1 4 4v22a4 4 0 0 1-4 4H40l-10 9v-9h-8a4 4 0 0 1-4-4V30a4 4 0 0 1 4-4z"/>
          <g fill="#fff" stroke="none"><circle cx="33" cy="41" r="3"/><circle cx="43" cy="41" r="3"/><circle cx="53" cy="41" r="3"/></g>
        </svg>
        <span class="tile-label">SNS</span>
      </a>
      <a class="tile tile--amber" href="#lesson">
        <svg class="tile-icon" viewBox="0 0 86 86" fill="none" stroke="#fff" stroke-width="3">
          <rect x="2" y="2" width="82" height="82" rx="16"/>
          <path d="M33 18c0 8 20 8 20 0"/>
          <path d="M33 24h20l2 12 8-4v8l-8 2 2 24H29l2-24-8-2v-8l8 4z"/>
          <rect x="37" y="48" width="12" height="8" rx="2"/>
        </svg>
        <span class="tile-label">Lesson<small>Class / Online</small></span>
      </a>
    </nav>
  </main>
</body>
</html>
```